Webdesign für visa-korvenet.org
Kreativer Initialvorschlag, schnelle Umsetzung, flexible Anpassung des Designvorschlags und nette Kommunikation, gerne wieder!
Zielgruppe
Wir vermitteln weltweit Reisegenehmigungen für Geschäfts- und Privatkunden. Auf VISA-Korvenet.org möchten wir auf deutsch, englisch & chinesisch Reisenden bei der Beiholung von Kurzzeit, Work & Travel & diversen Visaarten helfen.
Aufgabenstellung
Der Webseitezweck ist es, dass Besucher bestellen. Dafür muss die Seite attraktiv, einfach bedienbar und das CTA Element "zum Formular" präsent und mehrfach auftauchen.

```html
<!DOCTYPE html>
<html lang="de">
<head>
<meta charset="utf-8">
<title>VISA-Korvenet.org – eVisitor Visum Australien</title>
<link href="https://fonts.googleapis.com/css2?family=Roboto:wght@300;400;500;700&display=swap" rel="stylesheet">
<style>
:root{
  --navy:#0f3a73;
  --blue:#1d4f9a;
  --red:#b0121b;
  --text:#85898f;
  --heading:#2e3238;
  --bg:#f1f1f1;
  --card:#ffffff;
  --row-alt:#f4f4f4;
  --line:#e2e2e2;
  --footer:#2d2d2d;
  --footer-text:#c9c9c9;
  --bottom:#eeeeee;
}
*{box-sizing:border-box;margin:0;padding:0}
html,body{width:1200px;height:2216px;overflow:hidden}
body{font-family:"Roboto",Arial,sans-serif;font-weight:300;background:var(--bg);color:var(--text);font-size:9.2px;line-height:12.5px;position:relative}
.wrap{width:712px;margin:0 auto;position:relative}

/* hero */
.hero{position:relative;height:469px;overflow:hidden}
.hero-photo{position:absolute;inset:0;background:linear-gradient(180deg,#4a76c4 0%,#6f97d8 38%,#a8bfd9 62%,#c9c8c0 74%,#8a8f8d 82%,#2f5d93 90%,#1e4e86 100%)}
.site-header{position:relative;z-index:2;padding-top:12px}
.header-top{display:flex;justify-content:space-between;align-items:flex-start;height:47px;border-bottom:1px solid rgba(255,255,255,.35)}
.brand{display:flex;align-items:center;gap:6px;margin-top:10px;color:#fff;font-weight:500;font-size:13px;line-height:1}
.brand-dot{width:13px;height:13px;border-radius:50%;background:#fff}
.contact{text-align:right;color:#fff;font-size:11px;line-height:1.3}
.contact .phone{font-size:14px;display:flex;align-items:center;gap:6px;justify-content:flex-end;margin-top:4px}
.contact .hours{display:flex;align-items:center;gap:6px;justify-content:flex-end}
.main-nav{display:flex;justify-content:space-around;padding:10px 8px 0;font-size:11px;line-height:14px;color:#fff;font-weight:400}
.main-nav .active{color:#d8e6ff}
.hero-title{position:absolute;z-index:2;top:224px;left:0;right:0;text-align:center;color:#fff;font-size:38px;line-height:46px;font-weight:500;letter-spacing:.5px;text-shadow:0 1px 3px rgba(0,0,0,.3)}
.btn-red{position:absolute;z-index:2;top:280px;left:531px;width:137px;height:31px;background:var(--red);color:#fff;font-size:12px;font-weight:400;display:flex;align-items:center;justify-content:center}
.dots{position:absolute;z-index:2;top:451px;left:0;right:0;display:flex;justify-content:center;gap:5px}
.dots span{width:8px;height:8px;border-radius:50%;background:rgba(255,255,255,.55)}
.dots span:first-child{background:#fff}

/* cards */
.card{background:var(--card);box-shadow:0 1px 3px rgba(0,0,0,.08);margin-top:12px;padding:0 16px;overflow:hidden}
.card h2{font-weight:300;color:var(--heading);font-size:19px;line-height:24px;text-align:center}
.welcome{margin-top:18px;border-top:2px solid var(--navy);height:138px;text-align:center;padding:16px 24px 0}
.welcome h2 span{color:var(--blue)}
.welcome p{margin-top:6px}
.welcome p:first-of-type{margin-top:10px}
.compare{height:261px;padding-top:18px}
.compare-cols{display:flex;margin-top:14px}
.compare-col{flex:1;padding:0 16px 0 2px;position:relative;height:184px}
.compare-col+.compare-col{border-left:1px solid var(--line);padding-left:18px;padding-right:12px}
.col-title{display:flex;align-items:center;gap:10px;color:var(--heading);font-size:12.5px;line-height:16px;font-weight:300;margin-bottom:12px}
.icon{width:18px;height:18px;flex:none}
.btn-outline{position:absolute;bottom:0;left:50%;transform:translateX(-50%);width:125px;height:28px;border:1px solid var(--navy);color:var(--navy);font-size:11px;font-weight:400;display:flex;align-items:center;justify-content:center}
.docs{height:188px;padding-top:18px}
.docs .col-title{margin-bottom:16px}
.docs p+p,.docs ul+p{margin-top:12px}
.docs ul{list-style:none;margin-top:12px}
.faq{height:490px;padding-top:20px}
.faq h3{font-weight:300;color:var(--heading);font-size:12.5px;line-height:16px;margin:16px 0 6px}
.faq h3:first-child{margin-top:4px}
.faq p+p{margin-top:12px}
.faq b{color:var(--heading);font-weight:500}

/* table */
.benefits-title{text-align:center;font-size:20px;line-height:26px;font-weight:300;color:var(--heading);margin-top:26px;margin-bottom:13px}
.compare-table{width:712px;border-collapse:collapse;background:#fff;font-size:9.5px;line-height:12px}
.compare-table th{background:var(--navy);color:#fff;font-weight:400;font-size:11px;text-align:left;height:27px;padding:0 12px}
.compare-table td{height:24.5px;padding:0 12px;border-right:1px solid var(--line);white-space:nowrap}
.compare-table td.tick{text-align:center;color:var(--navy);font-size:13px;width:124px}
.compare-table tr:nth-child(even) td{background:var(--row-alt)}
.compare-table th+th{border-left:1px solid #2b578f;width:124px}

/* footer */
.site-footer{position:absolute;top:2049px;left:0;width:1200px;height:129px;background:var(--footer)}
.footer-cols{display:flex;gap:30px;padding-top:35px}
.footer-col{flex:1}
.footer-col h4{color:#e6e6e6;font-size:9.5px;line-height:12px;font-weight:500;text-transform:uppercase;padding-bottom:7px;border-bottom:1px solid #4a4a4a;margin-bottom:8px;letter-spacing:.2px;white-space:nowrap}
.footer-col p{color:var(--footer-text);font-size:9.5px;line-height:12.5px}
.cards{display:flex;gap:4px}
.cards span{width:29px;height:17px;border-radius:2px;background:#ececec}
.cards span:nth-child(2){background:#9a9a9a}
.cards span:nth-child(3){background:#4f8fd6}
.bottom-bar{position:absolute;top:2178px;left:0;width:1200px;height:38px;background:var(--bottom)}
.bottom-bar .wrap{display:flex;justify-content:space-between;align-items:center;height:38px;padding:0 10px;font-size:9.5px}
.legal a{color:var(--text);text-decoration:none;margin-left:16px}
.legal a:first-child{color:var(--blue)}
</style>
</head>
<body>

<section class="hero">
  <div class="hero-photo" role="img" aria-label="Foto: Skyline von Sydney mit Opernhaus am Hafen unter blauem Himmel"></div>
  <header class="site-header wrap">
    <div class="header-top">
      <div class="brand"><span class="brand-dot"></span>VISA Korvenet</div>
      <div class="contact">
        <div class="hours">
          <svg class="icon" viewBox="0 0 18 18" style="width:13px;height:13px"><circle cx="9" cy="9" r="7.5" fill="none" stroke="#fff" stroke-width="1.2"/><path d="M9 4.5V9l3 2" fill="none" stroke="#fff" stroke-width="1.2"/></svg>
          Mo-Fr 10-16 Uhr
        </div>
        <div class="phone">
          <svg class="icon" viewBox="0 0 18 18" style="width:14px;height:14px"><circle cx="9" cy="9" r="8" fill="none" stroke="#fff" stroke-width="1.2"/><path d="M6 5.5l1.5-.5 1 2-1 1c.5 1 1.4 1.9 2.4 2.4l1-1 2 1-.5 1.5c-3 .3-6.7-3.4-6.4-6.4z" fill="#fff"/></svg>
          0800 512904417
        </div>
      </div>
    </div>
    <nav class="main-nav">
      <span class="active">STARTSEITE</span><span>TOURISTEN VISUM</span><span>BUSINESS VISUM</span><span>WAS IST ETA</span><span>AGB</span><span>KONTAKT</span>
    </nav>
  </header>
  <h1 class="hero-title">EVISITOR VISUM AUSTRALIEN</h1>
  <a class="btn-red">REGISTRIEREN</a>
  <div class="dots"><span></span><span></span><span></span></div>
</section>

<main class="wrap">
  <section class="card welcome">
    <h2>Willkommen bei <span>VISA-Korvenet</span></h2>
    <p>visa-korvenet.org ist ein nicht staatlicher Servicedienstleister für die Beantragung von Evisitor-Genehmigungen.</p>
    <p>Bei uns erhalten Sie die Evisitor-Einreisegenehmigung einschließlich unserer Serviceleistung. Jeder Antrag wird von einem deutschsprachigen Support Mitarbeiter geprüft und bearbeitet. Damit Sie ohne Probleme, z.B. Formfehler, nach Australien einreisen können.</p>
    <p>Sofern Sie den Antrag über uns anfordern, ist dieser 12 Monate ab Ausstellung gültig, es sein denn Ihr Reisepass läuft vorher ab.</p>
  </section>

  <section class="card compare">
    <h2>Unterscheidung</h2>
    <div class="compare-cols">
      <div class="compare-col">
        <div class="col-title">
          <svg class="icon" viewBox="0 0 18 18"><circle cx="9" cy="9" r="8" fill="var(--navy)"/><path d="M9 5v9M6 7l3-2 3 2" stroke="#fff" stroke-width="1.4" fill="none"/></svg>
          eVisitor „Tourist ETA“ mit 12 Monaten Gültigkeit
        </div>
        <p>Mit dem Visitor Visum können Touristen bis zu drei Monaten am Stück nach Australien reisen um dort Urlaub zu machen, Verwandte oder Bekannte zu besuchen. Eine arbeitsbezogene Nutzung dieses Visums ist ausdrücklich <b style="color:var(--heading);font-weight:500">nicht</b> gestattet!<br>Wichtig: Es muss bereits vor Antritt der Reise ein gültiges Visum vorliegen. Drucken Sie Ihre eVisitor Nummer aus und legen Sie diese Ihren Reisedokumenten bei.</p>
        <a class="btn-outline">REGISTRIEREN</a>
      </div>
      <div class="compare-col">
        <div class="col-title">
          <svg class="icon" viewBox="0 0 18 18"><circle cx="9" cy="9" r="8" fill="var(--navy)"/><ellipse cx="9" cy="9" rx="3.5" ry="8" fill="none" stroke="#fff" stroke-width="1"/><path d="M1 9h16" stroke="#fff" stroke-width="1"/></svg>
          eVisitor „Business ETA“ mit 12 Monaten Gültigkeit
        </div>
        <p>Geschäftsreisende benötigen ein Business eVisitor Visum. Dieses ebenso elektronisch erstellte Visum hat eine Gültigkeit von 12 Monaten und kann für einen durchgängigen Geschäftsaufenthalt für bis zu drei Monaten genutzt werden. Wir empfehlen auch bei Messebesuchen ein Business Visum zu beantragen um eine problemlose Einreise zu gewährleisten.<br>Wichtig: Es muss bereits vor Antritt der Reise ein gültiges Business Visum vorliegen. Drucken Sie Ihre eVisitor Nummer aus und legen Sie diese Ihren Reisedokumenten bei.</p>
        <a class="btn-outline">REGISTRIEREN</a>
      </div>
    </div>
  </section>

  <section class="card docs">
    <div class="col-title">
      <svg class="icon" viewBox="0 0 18 22" style="height:22px"><rect x="0" y="0" width="18" height="22" rx="2" fill="var(--navy)"/><circle cx="9" cy="9" r="4.5" fill="none" stroke="#fff" stroke-width="1.1"/><path d="M4.5 9h9M9 4.5v9" stroke="#fff" stroke-width="1"/></svg>
      Welche Dokumente erhalte ich mit meinem Evisitor Visum?
    </div>
    <p>Sobald Ihre Evisitor Genehmigung erteilt worden ist erhalten Sie eine Bestätigung per Email. Dieses Dokument müssen Sie aufheben und mit Ihren Reisedokumenten zur Reise mitnehmen. Die Evisitor Dokumente umfassen</p>
    <ul>
      <li>• Ihre eVisitor Genehmigungsnummer</li>
      <li>• Das Datum ab dem Ihre eVisitor Nummer gültig ist</li>
      <li>• Die allgemeinen eVisitor Konditionen und Bedingungen</li>
    </ul>
    <p>Mit einer gültigen eVisitornummer (ETA Visum) erhalten Sie bei der Einreise nach Australien keinen Eintrag, bzw. Stempel mehr in Ihren Reisepass. Die Crew Ihrer Airline übermittelt bereits während des Fluges Ihre Pass und eVisitor Daten an die Australischen Behörden.</p>
  </section>

  <section class="card faq">
    <h3>Wann erhalte ich meine Evisitor ETA VISA Genehmigung?</h3>
    <p>Beide Evisitor Visa werden in der Regel umgehend gewährt, jedoch kann es in Ausnahmefällen zu einer Bearbeitungszeit von 2-10 Werktagen kommen. In äußerst seltenen Fällen kann eine Verweigerung einer Evisitor Genehmigung für die Einreise nach Australien auftreten. Diese wird jedoch schriftlich von den Australischen Behörden begründet. In diesem Fall empfehlen wir direkte Kontaktaufnahme mit der Australischen Botschaft in Berlin.</p>
    <h3>Was darf man als eVisitor (Inhaber eines ETA Visum) in Australien machen?</h3>
    <p>Als Tourist oder Geschäftsreisender dürfen Sie für den maximalen Zeitraum von drei Monaten ungehindert Australien bereisen. Die Evisitor Genehmigung gilt für ein Jahr, somit können wiederholte Reisen innerhalb dieses Zeitraums nach Australien unternommen werden. Die Australischen Behörden lassen darüber hinaus zu, dass eVisitor mit einem Touristen ETA Visum ehrenamtliche Tätigkeiten aufnehmen, solange diese ausschließlich unbezahlt (außer Essen, Nachtlager und geringfügiges Taschengeld) stattfinden und keinen vollbezahlten Arbeitsplatz eines australischen Staatsangehörigen gefährden oder gar ersetzten.<br>Australien gilt als liberales Land solange die Gesetze eingehalten werden. Unerlaubte Arbeiten, die Aufnahme von Studien oder Trainings darf nicht gegen Geld erfolgen und nicht länger wie drei Monate stattfinden.</p>
    <h3>3 Tipps für eine erfolgreiche Australien Reise</h3>
    <p>Gültige Reisedokumente für die gesamte Dauer des Aufenthaltes. Reisepass und vorläufiger Reisepass werden anerkannt. Kinder benötigen einen eigenen Reisepass. Personalausweis und vorläufiger Personalausweis sind nicht zugelassen Sollten asiatische Staaten im Zuge der Reise besucht werden wollen, informieren Sie sich bitte über die speziellen Vorschriften, da manche Staaten eine Gültigkeit bis zu sechs Monaten ausländischer Reisepässe voraussetzen.</p>
    <p>Australien hat sehr strikte Einreise und Quarantänevorschriften. An etlichen Flughäfen ist mit Körperscannern bei der Einreise zu rechnen. Ebenso müssen eingeführte Nahrungsmittel, Tier- und Pflanzenprodukte auf der Einreisekarte angegeben werden. Striktes Befolgen der Anweisungen wird von uns empfohlen um unnötige Wartezeiten und Ärger zu vermeiden.</p>
    <p>Halten Sie sich an die Gesetze des Landes. Wie bereits erwähnt ist Australien ein liberales Land, solange die Gesetze befolgt werden. Illegale Aktivitäten wie Verstöße gegen die Visa Bestimmungen, die Ausfuhr von kulturellen Schätzen oder die Einnahme von illegalen Substanzen können zur Ausweisung bis hin zu Freiheitstrafe in Australien führen.</p>
    <h3>Welche Staaten können Evisitor für Australien in Anspruch nehmen?</h3>
    <p>Andorra, Belgien, Brunei, Dänemark, <b>Deutschland</b>, Finnland, Frankreich, Griechenland, Großbritannien, Hong Kong, Irland, Island, Italien, Japan, Kanada, Liechtenstein, Luxemburg, Malaysia, Malta, Monaco, Niederlande, Nordirland, Norwegen, Österreich, Portugal, San Marino, Schweden, Schweiz, Singapur, Spanien, Südkorea, USA, Vatikan</p>
  </section>

  <h2 class="benefits-title">Ihre Vorteile mit www.visa-korvenet.org in der Übersicht</h2>
  <table class="compare-table">
    <tr><th>Unser Service</th><th>visa-korvenet.org</th><th>einreise-amt.gov</th></tr>
    <tr><td>Anmeldeformular auf deutsch</td><td class="tick">✓</td><td class="tick"></td></tr>
    <tr><td>Hilfe bei der Formulareingabe</td><td class="tick">✓</td><td class="tick"></td></tr>
    <tr><td>Email Support</td><td class="tick">✓</td><td class="tick"></td></tr>
    <tr><td>Auf Wunsch auch Sendung der ETA Nummer per Post</td><td class="tick">✓</td><td class="tick"></td></tr>
    <tr><td>FAQ Section</td><td class="tick">✓</td><td class="tick">✓</td></tr>
    <tr><td>Kontrolle Ihrer gemachten EingabenKontrolle Ihrer gemachten Eingaben</td><td class="tick">✓</td><td class="tick">✓</td></tr>
    <tr><td>Rückmeldung und Überprüfung ob Ihre Eingaben abgeschickt wurden</td><td class="tick">✓</td><td class="tick">✓</td></tr>
    <tr><td>Manuelle Kontrolle bei Falscheingaben und Rückmeldung durch Supportmitarbeiter</td><td class="tick">✓</td><td class="tick"></td></tr>
    <tr><td>Statusnachricht Ihres ETA-Antrages</td><td class="tick">✓</td><td class="tick"></td></tr>
    <tr><td>ETA-Nummer Versand bequem per PDF</td><td class="tick">✓</td><td class="tick"></td></tr>
    <tr><td>Aufbewahrung Ihrer ETA Nummer für ein Jahr</td><td class="tick">✓</td><td class="tick">✓</td></tr>
    <tr><td>Kostenlose Neuanforderung Ihrer ETA Nummer innerhalb eines Jahres bei Verlust</td><td class="tick">✓</td><td class="tick">✓</td></tr>
    <tr><td>Garantierte Rückerstattung der Gebührenkosten, falls Ihre ETA Genehmigung zurückgewiesen wird</td><td class="tick">✓</td><td class="tick"></td></tr>
  </table>
</main>

<footer class="site-footer">
  <div class="wrap footer-cols">
    <div class="footer-col"><h4>Informationen</h4><p>Gültigkeitsdauer ETA Visum</p></div>
    <div class="footer-col"><h4>Quicklinks</h4><p>ETA Formular deutsch<br>Was ist ETA</p></div>
    <div class="footer-col"><h4>Bearbeitungszeiten</h4><p>MO-DO 09.00 Uhr - 17.30 Uhr<br>FR 09.00 Uhr - 16.00 Uhr</p></div>
    <div class="footer-col"><h4>Zugelassene Zahlungsmittel</h4><div class="cards"><span></span><span></span><span></span></div></div>
  </div>
</footer>
<div class="bottom-bar">
  <div class="wrap">
    <span>© 2017 VISA Korvenet</span>
    <span class="legal"><a>Datenschutz</a><a>AGB</a><a>Impressum</a></span>
  </div>
</div>

</body>
</html>
```